Looking for amazing PowerPoint Design for sustainable, green last mile delivery company

What we need
- PowerPoint master (16:9)
- Min. 20-30 most used template slides
- Templates for tables, processes, gantt chart, etc.
- Would be good to make it look very modern, green/sustainable, human
- Feel free to extend the color range in addition to the 2 colors from our logo

Who we are
- https://www.brookvane-cargo.de/index1.php
- Brookvane Cargo is a pioneer in urban green logistics and provides zero-emissions last mile delivery services for its logistics and retail clients
- we take on urban parcel delivery for our clients with a 100% electric commercial vehicles fleet, fair and sustainable working conditions for our employees and a unique professional customer-focused mindset
- We see ourselves as a professional services company who strongly cares about the environment, clients and their customers, and its employees

Attachements
- Company logos - see attached
- Licensed pictures (feel free to use in the designs ) - see here: https://www.filemarsh.example/sh/82qptmzc61w304/XXPnRtfa9gg254hjKLDWQ7Mxo?dl=0

Requirements
Must have
• We are thinking about at least the following content templates:

- intro/outro (e.g., title, agenda, transition, team, goals, about us, executive summary, key take aways, thank you)
- charts and graphs (e.g., pie, doughnut, bar, line, waterfall, venn)
- image and video (e.g., image only, large image with a sentence)
- text (e.g., text only, text with graph, text with 3/4/5 categories, key numbers)
- process (e.g., steps, phases)
- funnels
- pyramid
- frameworks (with 2/3/4/5 categories)
- timeline (e.g., general/project timeline, gantt)
- services offer
- KPIs/scorecard
- vision, mission, values, culture
- evaluation results
- activities/ToDo page
- policy
- career path
- icons page

Hope this helps. Pls see this as wish list as some of them can also be built by the content from the other slides

```html
<!DOCTYPE html>
<html lang="en">
<head>
<meta charset="utf-8">
<title>Brookvane Cargo – Presentation Templates</title>
<link rel="stylesheet" href="https://fonts.googleapis.com/css2?family=Bebas+Neue&family=Montserrat:wght@400;600;700&display=swap">
<style>
:root{
  --green-dark:#1b8a2c;
  --green:#2ca637;
  --lime:#8cc63f;
  --lime-soft:#a4d34f;
  --ink:#333;
  --grey-text:#d5d5d5;
  --card:#f3f3f3;
  --board:#333333;
  --white:#fff;
}
*{box-sizing:border-box;margin:0;padding:0}
html,body{width:1200px;height:3000px;overflow:hidden}
body{font-family:"Montserrat",sans-serif;color:var(--ink);background:var(--board);position:relative}

.hero{position:absolute;left:0;top:0;width:1200px;height:804px;background:linear-gradient(#f4f4f4,#e9e9e9)}
.hero-slide{position:absolute;left:245px;top:112px;transform:scale(1.13);transform-origin:0 0;box-shadow:0 18px 40px rgba(0,0,0,.18)}

.board{position:absolute;left:0;top:804px;width:1200px;height:2196px;background:var(--board)}
.slide{position:absolute;width:545px;height:305px;background:var(--white);overflow:hidden}
.col-l{left:49px}.col-r{left:615px}
.row-1{top:59px}.row-2{top:402px}.row-3{top:751px}.row-4{top:1116px}

.slide-title{position:absolute;left:28px;top:12px;font-family:"Bebas Neue",sans-serif;font-size:36px;line-height:1.1;color:var(--green-dark);letter-spacing:.3px;font-weight:400}
.title-rule{position:absolute;left:18px;top:0;width:3px;height:50px;background:var(--green)}
.brand{position:absolute;right:16px;top:18px;display:flex;align-items:center;gap:6px}
.brand-dot{width:28px;height:28px;border-radius:50%;background:var(--green)}
.brand-name{font-family:"Bebas Neue",sans-serif;font-size:17px;color:var(--green);white-space:nowrap}

.footer{position:absolute;left:0;bottom:0;width:100%;height:30px;background:linear-gradient(90deg,var(--green-dark),var(--green) 60%,var(--lime));display:flex;align-items:center}
.footer-url{margin-left:14px;color:var(--white);font-size:11px;font-weight:600;letter-spacing:3.2px;white-space:nowrap}
.social{display:flex;gap:3px;margin-left:auto}
.social span{width:16px;height:16px;border-radius:50%;background:var(--lime-soft)}
.page-no{width:36px;height:30px;margin-left:14px;background:var(--lime);color:var(--white);font-size:10px;font-weight:700;display:flex;align-items:center;justify-content:center}

.small{font-size:6.2px;line-height:1.35;color:#555}
.label{font-size:6.5px;font-weight:700;color:var(--green)}

/* title slide */
.cover .brand{left:16px;right:auto;top:18px}
.cover .brand-dot{width:56px;height:56px}
.cover .brand-name{font-size:27px}
.cover-band{position:absolute;left:0;top:112px;width:262px;height:85px;background:var(--green-dark)}
.cover-head{position:absolute;left:18px;top:121px;font-family:"Bebas Neue",sans-serif;font-size:35px;line-height:1;color:var(--white);font-weight:400;white-space:nowrap}
.cover-strip{position:absolute;left:0;top:197px;width:302px;height:28px;background:var(--lime);color:var(--white);font-size:10px;font-weight:600;line-height:28px;padding-left:18px}
.cover-heart{position:absolute;left:240px;top:8px;width:310px;height:300px}
.cover-url{position:absolute;left:14px;top:276px;font-size:11px;font-weight:600;letter-spacing:3px;color:var(--ink)}
.cover .social{position:absolute;right:16px;top:274px}

/* agenda */
.agenda-heart{position:absolute;left:23px;top:68px;width:196px;height:186px}
.v-rule{position:absolute;left:259px;top:70px;width:1px;height:172px;background:#ccc}
.agenda-list{position:absolute;left:291px;top:73px;width:232px}
.agenda-list li{list-style:none;margin-bottom:11px}

/* table of content */
.toc-item{position:absolute;width:240px;display:flex;gap:10px;align-items:flex-start}
.toc-num{font-family:"Bebas Neue",sans-serif;font-size:44px;line-height:.9;color:var(--grey-text)}

/* about cards */
.card{position:absolute;top:68px;width:161px;height:183px;background:var(--card)}
.card-img{height:82px}
.card-label{height:16px;background:var(--lime);color:var(--white);font-size:7px;font-weight:700;text-align:center;line-height:16px;white-space:nowrap}
.card-text{padding:7px 8px;text-align:center;font-size:5.2px;line-height:1.38;color:#555}

/* infographic */
.hub{position:absolute;left:18px;top:72px;width:190px;height:190px}
.info-list{position:absolute;left:214px;top:60px;width:310px}
.info-list li{list-style:none;margin-bottom:9px}

/* pies */
.pie-intro{position:absolute;left:100px;top:63px;width:345px;text-align:center}
.pie{position:absolute;top:97px;width:140px;text-align:center}
.pie svg{display:block;margin:0 auto 6px}

/* bars */
.legend{position:absolute;right:40px;top:68px;display:flex;gap:10px;font-size:5px;color:#666}
.legend i{display:inline-block;width:5px;height:5px;border-radius:50%;margin-right:2px;vertical-align:middle}
.bar-chart{position:absolute;left:20px;top:76px;width:505px;height:180px}

/* services */
.svc-intro{position:absolute;left:20px;top:66px;width:505px;font-size:6px;line-height:1.35;color:#555}
.svc{position:absolute;top:99px;width:120px;height:157px;background:var(--card)}
.svc .card-img{height:82px}
.svc .card-label{font-size:5.8px}
.svc .card-text{font-size:5.4px}

/* contact */
.contact{position:absolute;left:48px;top:1489px;width:1115px;height:629px;background:var(--green);overflow:hidden}
.contact-brand{position:absolute;left:36px;top:40px;display:flex;align-items:center;gap:20px}
.contact-brand .brand-dot{width:110px;height:110px;background:var(--lime)}
.contact-brand .brand-name{font-size:52px;color:var(--white)}
.contact-band{position:absolute;left:0;top:197px;width:669px;height:326px;background:var(--lime-soft)}
.contact-title{position:absolute;left:38px;top:220px;font-family:"Bebas Neue",sans-serif;font-size:82px;line-height:1;color:var(--green-dark);font-weight:400}
.contact-info{position:absolute;left:38px;top:308px;font-size:24px;line-height:1.24;color:var(--white)}
.contact-info dt{font-weight:700;color:var(--green-dark)}
.contact-url{position:absolute;left:34px;top:564px;font-size:24px;font-weight:600;letter-spacing:7px;color:var(--white)}
.contact .social{position:absolute;right:36px;top:562px;gap:8px}
.contact .social span{width:36px;height:36px}
.contact-heart{position:absolute;left:494px;top:20px;width:623px;height:640px}
</style>
</head>
<body>

<section class="hero">
  <div class="slide cover hero-slide">
    <div class="brand"><span class="brand-dot"></span><span class="brand-name">Brookvane Cargo</span></div>
    <div class="cover-band"></div>
    <h1 class="cover-head">A Professional<br>Services Company</h1>
    <div class="cover-strip">BECAUSE WE CARE ABOUT TREES</div>
    <svg class="cover-heart" viewBox="0 0 100 92" preserveAspectRatio="none" role="img" aria-label="Photo of team hands holding a young seedling, framed in a heart">
      <defs><linearGradient id="gh1" x1="0" y1="0" x2="1" y2="1"><stop offset="0" stop-color="#a07850"/><stop offset=".5" stop-color="#c9a98a"/><stop offset="1" stop-color="#34456a"/></linearGradient></defs>
      <path d="M50 90 C22 68 2 48 2 26 C2 10 14 2 27 2 C38 2 46 9 50 19 C54 9 62 2 73 2 C86 2 98 10 98 26 C98 48 78 68 50 90Z" fill="url(#gh1)"/>
    </svg>
    <div class="cover-url">◍ www.brookvane-cargo.de</div>
    <div class="social"><span></span><span></span><span></span></div>
  </div>
</section>

<main class="board">

  <div class="slide cover col-l row-1">
    <div class="brand"><span class="brand-dot"></span><span class="brand-name">Brookvane Cargo</span></div>
    <div class="cover-band"></div>
    <h2 class="cover-head">A Professional<br>Services Company</h2>
    <div class="cover-strip">BECAUSE WE CARE ABOUT TREES</div>
    <svg class="cover-heart" viewBox="0 0 100 92" preserveAspectRatio="none" role="img" aria-label="Photo of team hands holding a young seedling, framed in a heart">
      <path d="M50 90 C22 68 2 48 2 26 C2 10 14 2 27 2 C38 2 46 9 50 19 C54 9 62 2 73 2 C86 2 98 10 98 26 C98 48 78 68 50 90Z" fill="url(#gh1)"/>
    </svg>
    <div class="cover-url">◍ www.brookvane-cargo.de</div>
    <div class="social"><span></span><span></span><span></span></div>
  </div>

  <div class="slide col-r row-1">
    <span class="title-rule"></span><h2 class="slide-title">Our Agenda</h2>
    <div class="brand"><span class="brand-dot"></span><span class="brand-name">Brookvane Cargo</span></div>
    <svg class="agenda-heart" viewBox="0 0 100 92" preserveAspectRatio="none" role="img" aria-label="Photo of a smiling team member with green tint, framed in a heart">
      <defs><linearGradient id="gh2" x1="0" y1="0" x2="1" y2="1"><stop offset="0" stop-color="#1f8a2e"/><stop offset=".6" stop-color="#6cb848"/><stop offset="1" stop-color="#176b22"/></linearGradient></defs>
      <path d="M50 90 C22 68 2 48 2 26 C2 10 14 2 27 2 C38 2 46 9 50 19 C54 9 62 2 73 2 C86 2 98 10 98 26 C98 48 78 68 50 90Z" fill="url(#gh2)"/>
    </svg>
    <span class="v-rule"></span>
    <ul class="agenda-list">
      <li><p class="label">AGENDA TEXT 1</p><p class="small">Lorem Ipsum is simply dummy text of the printing and typesetting industry. Lorem Ipsum has been the industry's standard dummy text ever since the 1500s.</p></li>
      <li><p class="label">AGENDA TEXT 2</p><p class="small">Lorem Ipsum is simply dummy text of the printing and typesetting industry. Lorem Ipsum has been the industry's standard dummy text ever since the 1500s.</p></li>
      <li><p class="label">AGENDA TEXT 3</p><p class="small">Lorem Ipsum is simply dummy text of the printing and typesetting industry. Lorem Ipsum has been the industry's standard dummy text ever since the 1500s.</p></li>
      <li><p class="label">AGENDA TEXT 4</p><p class="small">Lorem Ipsum is simply dummy text of the printing and typesetting industry. Lorem Ipsum has been the industry's standard dummy text ever since the 1500s.</p></li>
    </ul>
    <div class="footer"><span class="footer-url">◍ www.brookvane-cargo.de</span><div class="social"><span></span><span></span><span></span></div><span class="page-no">1</span></div>
  </div>

  <div class="slide col-l row-2">
    <span class="title-rule"></span><h2 class="slide-title">Table of Content</h2>
    <div class="brand"><span class="brand-dot"></span><span class="brand-name">Brookvane Cargo</span></div>
    <div class="toc-item" style="left:20px;top:73px"><span class="toc-num">01</span><div><p class="label">CONTENT HERE</p><p class="small">Lorem Ipsum is simply dummy text of the printing and typesetting industry. Lorem Ipsum has been the industry's standard dummy text ever.</p></div></div>
    <div class="toc-item" style="left:20px;top:143px"><span class="toc-num">02</span><div><p class="label">CONTENT HERE</p><p class="small">Lorem Ipsum is simply dummy text of the printing and typesetting industry. Lorem Ipsum has been the industry's standard dummy text ever.</p></div></div>
    <div class="toc-item" style="left:20px;top:213px"><span class="toc-num">03</span><div><p class="label">CONTENT HERE</p><p class="small">Lorem Ipsum is simply dummy text of the printing and typesetting industry. Lorem Ipsum has been the industry's standard dummy text ever.</p></div></div>
    <div class="toc-item" style="left:285px;top:73px"><span class="toc-num">04</span><div><p class="label">CONTENT HERE</p><p class="small">Lorem Ipsum is simply dummy text of the printing and typesetting industry. Lorem Ipsum has been the industry's standard dummy text ever.</p></div></div>
    <div class="toc-item" style="left:285px;top:143px"><span class="toc-num">05</span><div><p class="label">CONTENT HERE</p><p class="small">Lorem Ipsum is simply dummy text of the printing and typesetting industry. Lorem Ipsum has been the industry's standard dummy text ever.</p></div></div>
    <div class="toc-item" style="left:285px;top:213px"><span class="toc-num">06</span><div><p class="label">CONTENT HERE</p><p class="small">Lorem Ipsum is simply dummy text of the printing and typesetting industry. Lorem Ipsum has been the industry's standard dummy text ever.</p></div></div>
    <div class="footer"><span class="footer-url">◍ www.brookvane-cargo.de</span><div class="social"><span></span><span></span><span></span></div><span class="page-no">2</span></div>
  </div>

  <div class="slide col-r row-2">
    <span class="title-rule"></span><h2 class="slide-title">About Us</h2>
    <div class="brand"><span class="brand-dot"></span><span class="brand-name">Brookvane Cargo</span></div>
    <div class="card" style="left:21px">
      <div class="card-img" role="img" aria-label="Photo of an electric delivery van on a country road" style="background:linear-gradient(#cfe3f2,#9cc46a 60%,#5f8f3a)"></div>
      <div class="card-label">WHO WE ARE</div>
      <p class="card-text">Brookvane Cargo is a pioneer in urban green logistics and provides zero-emissions last mile delivery services for its logistics and retail clients. We take on urban parcel delivery for our clients with a 100% electric commercial vehicles fleet, fair and sustainable working conditions for our employees and a unique professional customer-focused mindset.</p>
    </div>
    <div class="card" style="left:192px">
      <div class="card-img" role="img" aria-label="Photo of hands holding a small tree" style="background:linear-gradient(#f2f4ef,#a9cf6a 55%,#d9b79a)"></div>
      <div class="card-label">OUR MISSION</div>
      <p class="card-text">To satisfy consumers' ever rising desire to buy products online, the CO2 emissions from delivery traffic will increase by 32% in the top 100 cities globally until 2030. Our clients care about our planet the same way we do, which is why Brookvane Cargo helps to make the planet a better place by running the most environmentally friendly urban last mile possible.</p>
    </div>
    <div class="card" style="left:363px">
      <div class="card-img" role="img" aria-label="Photo of a smiling professional in an office" style="background:linear-gradient(90deg,#c9ccd0,#e8e6e2 50%,#8a7f77)"></div>
      <div class="card-label">OUR VALUES</div>
      <p class="card-text">We see ourselves as a professional services company who strongly cares about the environment, clients and their customers, and its employees. We believe that delivering parcels CO2-free and providing a unique customer experience with a great team spirit are the cornerstones for Brookvane Cargo to operate in today's world in a sustainable yet profitable way.</p>
    </div>
    <div class="footer"><span class="footer-url">◍ www.brookvane-cargo.de</span><div class="social"><span></span><span></span><span></span></div><span class="page-no">3</span></div>
  </div>

  <div class="slide col-l row-3">
    <span class="title-rule"></span><h2 class="slide-title">Infographics</h2>
    <div class="brand"><span class="brand-dot"></span><span class="brand-name">Brookvane Cargo</span></div>
    <svg class="hub" viewBox="0 0 190 190" aria-hidden="true">
      <g fill="none" stroke="#2ca637" stroke-width="1.2">
        <path d="M60 95 C60 50 90 22 130 22"/><path d="M60 95 C60 140 90 170 130 170"/>
        <path d="M88 95 L130 70"/><path d="M88 95 L170 95"/><path d="M88 95 L130 125"/>
      </g>
      <circle cx="52" cy="95" r="50" fill="#e3e3e3"/>
      <circle cx="52" cy="95" r="39" fill="#8cc63f"/>
      <path d="M36 96 l11 11 l22 -24" fill="none" stroke="#fff" stroke-width="7" stroke-linecap="round" stroke-linejoin="round"/>
      <g fill="#fff" stroke="#8cc63f" stroke-width="2">
        <circle cx="130" cy="22" r="10"/><circle cx="130" cy="70" r="10"/><circle cx="170" cy="95" r="10"/><circle cx="130" cy="125" r="10"/><circle cx="130" cy="170" r="10"/>
      </g>
      <g fill="#2ca637"><circle cx="130" cy="22" r="4"/><circle cx="130" cy="70" r="4"/><circle cx="170" cy="95" r="4"/><circle cx="130" cy="125" r="4"/><circle cx="130" cy="170" r="4"/></g>
    </svg>
    <ul class="info-list">
      <li><p class="label">CONTENT HEADING</p><p class="small">Lorem Ipsum is simply dummy text of the printing and typesetting industry. Lorem Ipsum has been the industry's standard dummy text ever since the 1500s.</p></li>
      <li><p class="label">CONTENT HEADING</p><p class="small">Lorem Ipsum is simply dummy text of the printing and typesetting industry. Lorem Ipsum has been the industry's standard dummy text ever since the 1500s.</p></li>
      <li><p class="label">CONTENT HEADING</p><p class="small">Lorem Ipsum is simply dummy text of the printing and typesetting industry. Lorem Ipsum has been the industry's standard dummy text ever since the 1500s.</p></li>
      <li><p class="label">CONTENT HEADING</p><p class="small">Lorem Ipsum is simply dummy text of the printing and typesetting industry. Lorem Ipsum has been the industry's standard dummy text ever since the 1500s.</p></li>
      <li><p class="label">CONTENT HEADING</p><p class="small">Lorem Ipsum is simply dummy text of the printing and typesetting industry. Lorem Ipsum has been the industry's standard dummy text ever since the 1500s.</p></li>
    </ul>
    <div class="footer"><span class="footer-url">◍ www.brookvane-cargo.de</span><div class="social"><span></span><span></span><span></span></div><span class="page-no">4</span></div>
  </div>

  <div class="slide col-r row-3">
    <span class="title-rule"></span><h2 class="slide-title">Pie Charts</h2>
    <div class="brand"><span class="brand-dot"></span><span class="brand-name">Brookvane Cargo</span></div>
    <p class="pie-intro small">Lorem Ipsum is simply dummy text of the printing and typesetting industry. Lorem Ipsum has been the industry's standard dummy text ever since the 1500s.</p>
    <div class="pie" style="left:22px">
      <svg width="92" height="92" viewBox="0 0 92 92"><circle cx="46" cy="46" r="38" fill="none" stroke="#ddd" stroke-width="10"/><circle cx="46" cy="46" r="38" fill="none" stroke="#1b8a2c" stroke-width="10" stroke-dasharray="179 60" transform="rotate(-90 46 46)"/><text x="46" y="52" text-anchor="middle" font-family="Montserrat,sans-serif" font-size="15" font-weight="700" font-style="italic" fill="#777">75%</text></svg>
      <p class="label">CONTENT HEADING</p><p class="small">Lorem Ipsum is simply dummy text of the printing and typesetting industry. Lorem Ipsum has been the industry's standard dummy text ever</p>
    </div>
    <div class="pie" style="left:202px">
      <svg width="92" height="92" viewBox="0 0 92 92"><circle cx="46" cy="46" r="38" fill="none" stroke="#ddd" stroke-width="10"/><circle cx="46" cy="46" r="38" fill="none" stroke="#8cc63f" stroke-width="10" stroke-dasharray="155 84" transform="rotate(-90 46 46)"/><text x="46" y="52" text-anchor="middle" font-family="Montserrat,sans-serif" font-size="15" font-weight="700" font-style="italic" fill="#777">65%</text></svg>
      <p class="label">CONTENT HEADING</p><p class="small">Lorem Ipsum is simply dummy text of the printing and typesetting industry. Lorem Ipsum has been the industry's standard dummy text ever</p>
    </div>
    <div class="pie" style="left:382px">
      <svg width="92" height="92" viewBox="0 0 92 92"><circle cx="46" cy="46" r="38" fill="none" stroke="#ddd" stroke-width="10"/><circle cx="46" cy="46" r="38" fill="none" stroke="#2ca637" stroke-width="10" stroke-dasharray="119 120" transform="rotate(-90 46 46)"/><text x="46" y="52" text-anchor="middle" font-family="Montserrat,sans-serif" font-size="15" font-weight="700" font-style="italic" fill="#777">50%</text></svg>
      <p class="label">CONTENT HEADING</p><p class="small">Lorem Ipsum is simply dummy text of the printing and typesetting industry. Lorem Ipsum has been the industry's standard dummy text ever</p>
    </div>
    <div class="footer"><span class="footer-url">◍ www.brookvane-cargo.de</span><div class="social"><span></span><span></span><span></span></div><span class="page-no">5</span></div>
  </div>

  <div class="slide col-l row-4">
    <span class="title-rule"></span><h2 class="slide-title">Bar Charts</h2>
    <div class="brand"><span class="brand-dot"></span><span class="brand-name">Brookvane Cargo</span></div>
    <div class="legend"><span><i style="background:#e3e3e3"></i>Receipts</span><span><i style="background:#8cc63f"></i>Sales</span><span><i style="background:#1b8a2c"></i>Orders</span></div>
    <svg class="bar-chart" viewBox="0 0 505 180" font-family="Montserrat,sans-serif" font-size="4.5" fill="#666">
      <g stroke="#eee" stroke-width=".6">
        <line x1="20" y1="10" x2="500" y2="10"/><line x1="20" y1="26" x2="500" y2="26"/><line x1="20" y1="42" x2="500" y2="42"/><line x1="20" y1="58" x2="500" y2="58"/><line x1="20" y1="74" x2="500" y2="74"/><line x1="20" y1="90" x2="500" y2="90"/><line x1="20" y1="106" x2="500" y2="106"/><line x1="20" y1="122" x2="500" y2="122"/><line x1="20" y1="138" x2="500" y2="138"/><line x1="20" y1="154" x2="500" y2="154"/>
      </g>
      <line x1="20" y1="170" x2="500" y2="170" stroke="#bbb" stroke-width=".6"/>
      <g text-anchor="end"><text x="12" y="12">100</text><text x="12" y="28">90</text><text x="12" y="44">80</text><text x="12" y="60">70</text><text x="12" y="76">60</text><text x="12" y="92">50</text><text x="12" y="108">40</text><text x="12" y="124">30</text><text x="12" y="140">20</text><text x="12" y="156">10</text><text x="12" y="172">0</text></g>
      <g>
        <rect x="30" y="155" width="22" height="15" fill="#e3e3e3"/><rect x="30" y="139" width="22" height="16" fill="#1b8a2c"/><rect x="30" y="124" width="22" height="15" fill="#8cc63f"/>
        <rect x="69" y="125" width="22" height="45" fill="#e3e3e3"/><rect x="69" y="77" width="22" height="48" fill="#1b8a2c"/><rect x="69" y="26" width="22" height="51" fill="#8cc63f"/>
        <rect x="108" y="155" width="22" height="15" fill="#e3e3e3"/><rect x="108" y="135" width="22" height="20" fill="#1b8a2c"/><rect x="108" y="77" width="22" height="58" fill="#8cc63f"/>
        <rect x="147" y="158" width="22" height="12" fill="#e3e3e3"/><rect x="147" y="10" width="22" height="148" fill="#1b8a2c"/>
        <rect x="186" y="100" width="22" height="70" fill="#e3e3e3"/><rect x="186" y="42" width="22" height="58" fill="#8cc63f"/>
        <rect x="225" y="155" width="22" height="15" fill="#e3e3e3"/><rect x="225" y="134" width="22" height="21" fill="#1b8a2c"/>
        <rect x="264" y="125" width="22" height="45" fill="#e3e3e3"/><rect x="264" y="83" width="22" height="42" fill="#1b8a2c"/><rect x="264" y="42" width="22" height="41" fill="#8cc63f"/>
        <rect x="303" y="150" width="22" height="20" fill="#e3e3e3"/><rect x="303" y="26" width="22" height="124" fill="#1b8a2c"/>
        <rect x="342" y="155" width="22" height="15" fill="#e3e3e3"/><rect x="342" y="97" width="22" height="58" fill="#8cc63f"/>
        <rect x="381" y="125" width="22" height="45" fill="#e3e3e3"/><rect x="381" y="58" width="22" height="67" fill="#1b8a2c"/>
        <rect x="420" y="110" width="22" height="60" fill="#e3e3e3"/><rect x="420" y="42" width="22" height="68" fill="#8cc63f"/>
        <rect x="459" y="155" width="22" height="15" fill="#e3e3e3"/><rect x="459" y="108" width="22" height="47" fill="#1b8a2c"/>
      </g>
      <g text-anchor="middle"><text x="41" y="178">JAN</text><text x="80" y="178">FEB</text><text x="119" y="178">MAR</text><text x="158" y="178">APR</text><text x="197" y="178">MAY</text><text x="236" y="178">JUN</text><text x="275" y="178">JUL</text><text x="314" y="178">AUG</text><text x="353" y="178">SEP</text><text x="392" y="178">OCT</text><text x="431" y="178">NOV</text><text x="470" y="178">DEC</text></g>
    </svg>
    <div class="footer"><span class="footer-url">◍ www.brookvane-cargo.de</span><div class="social"><span></span><span></span><span></span></div><span class="page-no">6</span></div>
  </div>

  <div class="slide col-r row-4">
    <span class="title-rule"></span><h2 class="slide-title">Our Services</h2>
    <div class="brand"><span class="brand-dot"></span><span class="brand-name">Brookvane Cargo</span></div>
    <p class="svc-intro">Brookvane Cargo provides last mile delivery services in urban areas to clients in the logistics and retail space. Our permanent employees are all highly trained and commit to highest professional standards which we continuously review and further develop with them.</p>
    <div class="svc" style="left:20px">
      <div class="card-img" role="img" aria-label="Photo of a green electric van on a city road" style="background:linear-gradient(135deg,#dfe8ee,#7bb94a 55%,#3f5f48)"></div>
      <div class="card-label">ZERO-EMISSION DELIVERY</div>
      <p class="card-text">We operate a 100% electric commercial vehicle fleet</p>
    </div>
    <div class="svc" style="left:146px">
      <div class="card-img" role="img" aria-label="Photo of two professionals shaking hands" style="background:linear-gradient(135deg,#8fa6b8,#d7c2ad 50%,#4a5a6c)"></div>
      <div class="card-label">PROFESSIONAL ALL AROUND</div>
      <p class="card-text">We honor our commitments and hold ourselves to the highest professional standards</p>
    </div>
    <div class="svc" style="left:272px">
      <div class="card-img" role="img" aria-label="Photo of a delivery driver holding parcels" style="background:linear-gradient(135deg,#b9b3aa,#2f4a7a 55%,#c2a07a)"></div>
      <div class="card-label">HIGHLY TRAINED DRIVERS</div>
      <p class="card-text">We only employ permanently, train far above average, and live a great team spirit</p>
    </div>
    <div class="svc" style="left:398px">
      <div class="card-img" role="img" aria-label="Photo of a customer service agent with headset" style="background:linear-gradient(135deg,#6f8fb0,#eef1f4 55%,#c7cdd4)"></div>
      <div class="card-label">RARE CUSTOMER FOCUS</div>
      <p class="card-text">We live a customer-oriented mindset, always measuring ourselves against their experience</p>
    </div>
    <div class="footer"><span class="footer-url">◍ www.brookvane-cargo.de</span><div class="social"><span></span><span></span><span></span></div><span class="page-no">7</span></div>
  </div>

  <div class="contact">
    <div class="contact-brand"><span class="brand-dot"></span><span class="brand-name">Brookvane Cargo</span></div>
    <div class="contact-band"></div>
    <h2 class="contact-title">Contact Us</h2>
    <dl class="contact-info">
      <dt>LOCATION:</dt><dd>Lindenhof Strasse 48, 10999 Berlin</dd>
      <dt>EMAIL ADDRESS :</dt><dd>info(at)brookvane-cargo.de</dd>
      <dt>PHONE NUMBER:</dt><dd>+49 (0) 30 5550 1284</dd>
    </dl>
    <svg class="contact-heart" viewBox="0 0 100 92" preserveAspectRatio="none" role="img" aria-label="Photo looking up a tall tree trunk into a green leafy canopy, framed in a heart">
      <defs><radialGradient id="gh3" cx=".55" cy=".45" r=".7"><stop offset="0" stop-color="#d9ec8a"/><stop offset=".45" stop-color="#7fbf3a"/><stop offset="1" stop-color="#2e6a1e"/></radialGradient></defs>
      <path d="M50 90 C22 68 2 48 2 26 C2 10 14 2 27 2 C38 2 46 9 50 19 C54 9 62 2 73 2 C86 2 98 10 98 26 C98 48 78 68 50 90Z" fill="url(#gh3)"/>
    </svg>
    <div class="contact-url">◍ www.brookvane-cargo.de</div>
    <div class="social"><span></span><span></span><span></span></div>
  </div>

</main>
</body>
</html>
```